Training Consultant for Oil and Gas Drillers needs logo for business cards

I teach oil and gas professionals the skills required to keep rigs from blowing up. The company name is "Night Shift Bore Safety", which is pronounced Night Shyft. Tour refers to the time on an oil rig when a worker is off for sleep and rest. I teach something called Well Control, which is how to maintain a pressure balance in the well so the hydro carbons don't come to surface unexpectedly( like the Silver Tide Platform).

Target Market(s)

Rig hands and oil companies

Contact Information for Business Card

Night Shift BS ( company name) with a new logo
My name (Dale Ferrington )and Title (Well Control Consultant)
Phone number and address

Font styles to use
Serif
Sans Serif

Colors

Designer to choose colors to be used in the design.

Requirements
Must have
• I need a logo for the company. I do not have anything yet

```html
<!DOCTYPE html>
<html lang="en">
<head>
<meta charset="utf-8">
<title>Night Shift BS – Business Card</title>
<link rel="stylesheet" href="https://fonts.googleapis.com/css2?family=Lato:ital,wght@0,400;0,700;1,400&family=Montserrat:wght@800&display=swap">
<style>
  :root {
    --card: #ebebeb;
    --orange: #d38d36;
    --ink: #1c1c1c;
    --white: #ffffff;
  }
  * { margin: 0; padding: 0; box-sizing: border-box; }
  html, body { width: 1200px; height: 655px; overflow: hidden; background: var(--card); }
  .card { position: relative; width: 1200px; height: 655px; background: var(--card); font-family: "Lato", sans-serif; color: var(--ink); }

  .holder-name { position: absolute; left: 40px; top: 52px; font-size: 58px; font-weight: 400; letter-spacing: -0.5px; line-height: 1; }
  .holder-name .first { color: var(--orange); }
  .holder-name .last { color: var(--ink); }
  .holder-title { position: absolute; left: 42px; top: 120px; font-size: 28px; font-style: italic; }

  .divider { position: absolute; top: 268px; height: 8px; }
  .divider-long { left: 40px; width: 420px; background: var(--ink); }
  .divider-short { left: 468px; width: 64px; height: 7px; background: var(--orange); }

  .contacts { position: absolute; left: 38px; top: 340px; list-style: none; }
  .contact { display: flex; align-items: center; height: 40px; margin-bottom: 13px; font-size: 29px; }
  .contact-icon { width: 40px; height: 40px; margin-right: 24px; flex: none; }

  .address-band { position: absolute; left: 0; top: 527px; width: 1200px; height: 93px; }
  .address { position: absolute; left: 38px; top: 551px; display: flex; align-items: center; font-size: 29px; font-style: italic; color: var(--white); }
  .address .contact-icon { margin-right: 24px; }

  .brand { position: absolute; left: 660px; top: 160px; width: 440px; display: flex; flex-direction: column; align-items: center; }
  .brand-dot { width: 150px; height: 150px; border-radius: 50%; background: var(--orange); margin-bottom: 60px; }
  .brand-name { font-family: "Montserrat", sans-serif; font-weight: 800; font-size: 54px; color: var(--ink); white-space: nowrap; line-height: 1; }
</style>
</head>
<body>
<div class="card">
  <h1 class="holder-name"><span class="first">DALE</span> <span class="last">FERRINGTON</span></h1>
  <p class="holder-title">Well Control Consultant</p>

  <div class="divider divider-long"></div>
  <div class="divider divider-short"></div>

  <ul class="contacts">
    <li class="contact">
      <svg class="contact-icon" viewBox="0 0 40 40" aria-hidden="true">
        <circle cx="20" cy="20" r="20" fill="var(--orange)"/>
        <path d="M11 17c0-3 4-5 9-5s9 2 9 5v2h-5v-2h-8v2h-5z" fill="var(--white)"/>
        <rect x="13" y="20" width="14" height="8" rx="2" fill="var(--white)"/>
      </svg>
      <span>000 1234 5678</span>
    </li>
    <li class="contact">
      <svg class="contact-icon" viewBox="0 0 40 40" aria-hidden="true">
        <circle cx="20" cy="20" r="20" fill="var(--orange)"/>
        <rect x="11" y="13" width="18" height="14" fill="none" stroke="var(--white)" stroke-width="2"/>
        <path d="M11 13l9 8 9-8" fill="none" stroke="var(--white)" stroke-width="2"/>
      </svg>
      <span>email@nightshiftbs.com</span>
    </li>
    <li class="contact">
      <svg class="contact-icon" viewBox="0 0 40 40" aria-hidden="true">
        <circle cx="20" cy="20" r="20" fill="var(--orange)"/>
        <rect x="11" y="12" width="18" height="12" fill="none" stroke="var(--white)" stroke-width="2"/>
        <path d="M16 28h8M20 24v4" stroke="var(--white)" stroke-width="2"/>
      </svg>
      <span>www.nightshiftboresafety.com</span>
    </li>
  </ul>

  <svg class="address-band" viewBox="0 0 1200 93" aria-hidden="true">
    <path d="M0 0H826a10 10 0 0 1 9 14L812 84a14 14 0 0 1-13 9H0z" fill="var(--orange)"/>
    <path d="M870 0H1200V93H852a8 8 0 0 1-7-11L858 8a14 14 0 0 1 12-8z" fill="var(--ink)"/>
  </svg>
  <p class="address">
    <svg class="contact-icon" viewBox="0 0 40 40" aria-hidden="true">
      <circle cx="20" cy="20" r="20" fill="var(--white)"/>
      <path d="M20 30s-7-8-7-13a7 7 0 0 1 14 0c0 5-7 13-7 13z" fill="var(--orange)"/>
      <circle cx="20" cy="17" r="2.6" fill="var(--white)"/>
    </svg>
    <span>21 St. Your Address here, 500</span>
  </p>

  <div class="brand">
    <div class="brand-dot"></div>
    <p class="brand-name">Night Shift BS</p>
  </div>
</div>
</body>
</html>
```